BOOK COVER (6 X 9) FOR CARNFIELD MOOR BOOKS

Book title: SEASONS OF GLASS; Author: TOMAS R. VELUNDE

This is the story of a man who grew up in Saudi Arabia in the 1940s, was schooled around the world. He survived death many times, once during the revolution in Bangladesh in the 1970s. Although a Pakistani, he knew Saudi royalty and worked there for most of his life. A lot of mystical things happened to him. SORRY TO BE SO VAGUE.

Book size will be 6 x 9

Target Market(s)

Adults interested in immigrant stories; the unexplainable; whimsical memoirs

Requirements
Nice to have
• This is a man who lived in many different worlds and countries. He lived through the Bangladesh revolution and other life threatening events.
Should not have
• Arabic dress -- he wore white suits

```html
<!DOCTYPE html>
<html lang="en">
<head>
<meta charset="utf-8">
<title>Seasons of Glass — Tomas R. Velunde</title>
<link rel="stylesheet" href="https://fonts.googleapis.com/css2?family=Cinzel:wght@400;500&family=EB+Garamond:ital,wght@1,400;1,500&display=swap">
<style>
  :root {
    --paper: #ffffff;
    --ink: #111111;
    --red: #ff1a1a;
    --green: #1e8a1e;
    --yellow: #eef51c;
    --cover-light: #c9d5d9;
    --cover-mid: #aebcc2;
    --cover-dark: #94a3aa;
    --imprint-bg: #5e5b5e;
    --imprint-text: #f2f2f2;
  }
  * { margin: 0; padding: 0; box-sizing: border-box; }
  html, body { width: 1200px; height: 900px; overflow: hidden; background: var(--paper); }
  .cover { position: relative; width: 1200px; height: 900px; overflow: hidden; background: var(--paper); }

  .author {
    position: absolute; right: 365px; top: 78px;
    font-family: "EB Garamond", Georgia, serif; font-style: italic; font-weight: 400;
    font-size: 62px; line-height: 74px; letter-spacing: 6px; text-align: right;
    color: var(--red); text-transform: uppercase;
  }
  .author .initial { color: var(--ink); }

  .imprint {
    position: absolute; left: 975px; top: 0; width: 225px; height: 212px;
    background: var(--imprint-bg);
    display: flex; align-items: center; justify-content: center; text-align: center;
    font-family: "Cinzel", "Times New Roman", serif; font-weight: 400;
    font-size: 24px; line-height: 34px; letter-spacing: 2px; color: var(--imprint-text);
  }

  .artwork {
    position: absolute; left: 0; top: 245px; width: 1005px; height: 655px; overflow: hidden;
    background: linear-gradient(90deg, var(--cover-light) 0%, var(--cover-mid) 19%, var(--cover-dark) 20.5%, var(--cover-light) 23%, var(--cover-mid) 70%, var(--cover-light) 100%);
    box-shadow: 8px 0 10px rgba(0,0,0,0.25);
  }
  .title-top, .title-bottom {
    position: absolute; left: 98px; white-space: nowrap;
    font-family: "Cinzel", "Times New Roman", serif; font-weight: 400;
  }
  .title-top { top: -35px; font-size: 128px; line-height: 140px; letter-spacing: 46px; color: var(--green); }
  .title-bottom { top: 580px; font-size: 150px; line-height: 160px; letter-spacing: 36px; color: var(--red); }
  .title-middle {
    position: absolute; left: 360px; top: 92px; white-space: nowrap;
    font-family: "EB Garamond", Georgia, serif; font-style: italic; font-weight: 400;
    font-size: 100px; line-height: 100px; color: var(--ink); letter-spacing: 8px;
  }
  .accent { position: absolute; left: 0; top: 0; pointer-events: none; }
</style>
</head>
<body>
<main class="cover">
  <p class="author">Tomas<br><span class="initial">R.</span> Velunde</p>

  <div class="imprint">Carnfield<br>Moor<br>Books</div>

  <section class="artwork" role="img" aria-label="Photograph of a pale blue-grey book lying open, showing its spine fold">
    <h1 class="title-top">SEASONS</h1>
    <p class="title-middle">of glass</p>
    <p class="title-bottom">SEASONS</p>
  </section>

  <svg class="accent" width="1200" height="900" viewBox="0 0 1200 900" aria-hidden="true">
    <path d="M500 590 C500 558 540 540 585 540 C640 540 668 556 668 580 C668 608 630 612 580 610 C530 608 500 612 500 590 Z"
          fill="var(--yellow)"/>
  </svg>
</main>
</body>
</html>
```